Afternoon Soiree Garden Party Invitation

Invitation design for an 'Afternoon Soirée' backyard garden party.
Format is for-print and mailing and can be either double-sided design to be enveloped and mailed or it can be a postcard-style with design on one side and address/postage placeholder on the reverse side.
Text, dimensions and additional information in the provided Word document.
Font styles to use
Script
Requirements
Must have
- Elegant, yet easy-going and warm/welcoming feel

```html
<!DOCTYPE html>
<html lang="en">
<head>
<meta charset="utf-8">
<title>Afternoon Soiree Invitation</title>
<link rel="stylesheet" href="https://fonts.googleapis.com/css2?family=Pacifico&family=Patrick+Hand+SC&family=Roboto+Slab:wght@400;500&family=Special+Elite&display=swap">
<style>
  :root {
    --page-bg: #ece8e1;
    --sky-top: #586a62;
    --sky-mid: #8e9a8a;
    --paper: #ddd4c1;
    --ink-navy: #1f2b40;
    --ink-rust: #8b5b4b;
    --rule: #6f6457;
    --leaf-sage: #a9bcb0;
    --leaf-mauve: #b3a0ad;
    --light-glow: #f2d88a;
  }
  * { margin: 0; padding: 0; box-sizing: border-box; }
  html, body {
    width: 1200px; height: 1200px; overflow: hidden;
    background: var(--page-bg);
  }
  .invitation {
    position: absolute; left: 210px; top: 50px;
    width: 780px; height: 1100px;
    background: linear-gradient(180deg, var(--sky-top) 0%, var(--sky-mid) 40%, var(--paper) 78%, var(--paper) 100%);
    box-shadow: 0 6px 24px rgba(0,0,0,0.18);
    overflow: hidden;
  }
  .string-lights {
    position: absolute; right: 0; top: 0; width: 420px; height: 200px;
    background: radial-gradient(ellipse at 70% 45%, rgba(242,216,138,0.28), rgba(242,216,138,0) 70%);
  }
  .foliage {
    position: absolute; left: 0; bottom: 0; width: 780px; height: 480px;
    background:
      radial-gradient(ellipse at 8% 80%, rgba(169,188,176,0.75), rgba(169,188,176,0) 55%),
      radial-gradient(ellipse at 25% 95%, rgba(179,160,173,0.55), rgba(179,160,173,0) 50%),
      radial-gradient(ellipse at 85% 100%, rgba(169,188,176,0.45), rgba(169,188,176,0) 35%);
  }
  .line { position: absolute; left: 0; width: 100%; text-align: center; color: var(--ink-navy); }
  .lead-in { top: 285px; font-family: "Patrick Hand SC", cursive; font-size: 27px; letter-spacing: 1px; }
  .article { top: 318px; font-family: "Pacifico", cursive; font-size: 34px; }
  .event-title { top: 352px; font-family: "Pacifico", cursive; font-size: 72px; letter-spacing: -1px; }
  .date-row {
    position: absolute; top: 540px; left: 0; width: 100%;
    display: flex; justify-content: center; align-items: center; gap: 14px;
    color: var(--ink-rust); font-family: "Roboto Slab", serif;
  }
  .date-side {
    font-size: 25px; font-weight: 500; padding: 8px 2px;
    border-top: 1.5px solid var(--rule); border-bottom: 1.5px solid var(--rule);
    letter-spacing: 1px;
  }
  .date-main { text-align: center; line-height: 0.95; }
  .date-month { display: block; font-size: 36px; }
  .date-day { display: block; font-size: 54px; }
  .venue { top: 655px; font-family: "Patrick Hand SC", cursive; font-size: 42px; letter-spacing: 2px; }
  .address { top: 712px; font-family: "Special Elite", monospace; font-size: 22px; }
  .note { font-family: "Patrick Hand SC", cursive; font-size: 27px; letter-spacing: 1px; }
  .note-weather { top: 883px; }
  .note-call { top: 920px; }
  .age-notice {
    position: absolute; top: 972px; left: 50%; transform: translateX(-50%);
    padding: 4px 14px; border-top: 1.5px solid var(--rule); border-bottom: 1.5px solid var(--rule);
    font-family: "Patrick Hand SC", cursive; font-size: 28px; color: var(--ink-navy); letter-spacing: 1px;
    white-space: nowrap;
  }
  .age-notice .age { font-size: 36px; }
</style>
</head>
<body>
  <main class="invitation">
    <div class="string-lights" role="img" aria-label="Strand of glowing string lights across the top corner"></div>
    <div class="foliage" role="img" aria-label="Watercolour sage and mauve leaves along the bottom"></div>

    <p class="line lead-in">Join us for</p>
    <p class="line article">an</p>
    <h1 class="line event-title">Afternoon Soiree</h1>

    <div class="date-row">
      <span class="date-side">FRIDAY</span>
      <span class="date-main"><span class="date-month">Jul</span><span class="date-day">17</span></span>
      <span class="date-side">4-8 PM</span>
    </div>

    <p class="line venue">The Marlowe Residence</p>
    <p class="line address">248 Linden Row</p>

    <p class="line note note-weather">Weather permitting.</p>
    <p class="line note note-call">Please call 555-214-7390 if unsure.</p>
    <p class="age-notice">this is a <span class="age">19+</span> event</p>
  </main>
</body>
</html>
```